I need the Scorecard I've developed for my staff to be produced into a visually engaging piece that will encourage the staff to utilize it on a daily basis. I'm thinking it could be 5x7 in size so that it isn't too cumbersome, but I'm open to different layouts.
I have multiple other departments that will need Scorecards created for them as well, but each one will contain task specific questions for each department.

```html
<!DOCTYPE html>
<html lang="en">
<head>
<meta charset="utf-8">
<title>Receptionist Daily Scorecard</title>
<link rel="stylesheet" href="https://fonts.googleapis.com/css2?family=Arimo:wght@400;700&family=Roboto+Condensed:wght@400&display=swap">
<style>
:root{
  --frame:#e0352b;
  --bar-dark:#5f5b5a;
  --green-head:#acd062;
  --green-row:#d2e6a2;
  --peach-head:#ebc19c;
  --peach-row:#f2d8c1;
  --grey-row:#dedede;
  --teal-head:#84c19d;
  --teal-row:#c9e3cf;
  --orange-head:#eea052;
  --orange-row:#f3cfa8;
  --plum-head:#9b3f75;
  --plum-row:#dfc5da;
  --sign-border:#1b5ea8;
  --ink:#1e1e1e;
  --icon-brown:#7a3b2a;
}
*{box-sizing:border-box;margin:0;padding:0}
html,body{width:1057px;height:1200px;overflow:hidden;background:#fff}
body{font-family:"Arimo",Arial,sans-serif;color:var(--ink)}
.scorecard{position:relative;width:1057px;height:1200px;border:2px solid var(--frame);background:#fff}
.block{position:absolute;left:29px;width:999px}
.bar{height:38px;border-radius:20px 20px 0 0;background:var(--bar-dark);color:#fff;font-weight:700;font-size:26px;display:flex;align-items:center;justify-content:center;gap:12px;position:relative;white-space:nowrap}
.bar .icon{position:absolute;top:-10px}
.grid-row{display:grid;grid-template-columns:454px 124px 1fr;gap:3px;margin-top:3px;height:37px}
.grid-row>div{display:flex;align-items:center;font-size:22px;white-space:nowrap;overflow:hidden}
.grid-row>div:first-child{padding-left:18px}
.head>div{font-size:23px}
.head .rating{font-family:"Roboto Condensed",sans-serif;font-size:22px;padding-left:4px}
.head .rating span{display:inline-block;transform:scaleX(.86);transform-origin:left center}
.head .notes{justify-content:center}
.dc .head>div{background:var(--green-head)}
.dc .row>div{background:var(--green-row)}
.routing .head>div{background:var(--peach-head)}
.routing .row>div{background:var(--peach-row)}
.status-row{height:37px;margin-top:3px;background:var(--grey-row);display:flex;align-items:center;font-size:21.5px;position:relative;white-space:nowrap}
.status-row .tick{position:absolute;left:71px;width:29px;height:29px;border-radius:50%;background:#fff}
.status-row .level{position:absolute;left:136px}
.status-row .desc{position:absolute;left:340px}
.line-row{height:37px;margin-top:3px;display:flex;align-items:center;font-size:20.5px;padding:0 49px 0 48px;white-space:nowrap}
.line-row .fill{flex:1;border-bottom:1px dotted #444;margin:14px 0 0 4px}
.reflection .bar{background:var(--teal-head)}
.reflection .line-row{background:var(--teal-row);font-family:"Roboto Condensed",sans-serif;font-size:22px}
.flags .bar{background:var(--orange-head);gap:8px}
.flags .line-row{background:var(--orange-row);padding-left:24px;padding-right:23px}
.flags .line-row svg{margin-right:10px;flex:none}
.manager{width:584px}
.manager .bar{background:var(--plum-head)}
.manager .line-row{background:var(--plum-row);padding-left:41px;padding-right:160px}
.sign-box{position:absolute;left:629px;top:1054px;width:399px;height:118px;border:2px solid var(--sign-border);border-radius:12px;padding:0 14px 0 14px;font-family:"Roboto Condensed",sans-serif;font-size:23px;white-space:nowrap}
.sign-line{display:flex;align-items:flex-end;height:36px}
.sign-line .label{width:168px;flex:none}
.sign-line .label.right{text-align:right}
.sign-line .fill{flex:1;border-bottom:1px dotted #444;margin:0 0 6px 6px}
</style>
</head>
<body>
<main class="scorecard">

  <section class="block dc" style="top:36px">
    <div class="bar">
      <span class="icon" style="left:313px" role="img" aria-label="Certificate icon">
        <svg width="38" height="42"><rect x="3" y="2" width="32" height="38" rx="4" fill="none" stroke="#8cc63f" stroke-width="2.5"/><circle cx="12" cy="18" r="5" fill="none" stroke="#8cc63f" stroke-width="2"/><line x1="20" y1="14" x2="30" y2="14" stroke="#8cc63f" stroke-width="2"/><line x1="20" y1="20" x2="30" y2="20" stroke="#8cc63f" stroke-width="2"/><line x1="10" y1="29" x2="30" y2="29" stroke="#8cc63f" stroke-width="2"/></svg>
      </span>
      <span>5. Death Certificates</span>
    </div>
    <div class="grid-row head"><div>Task</div><div class="rating"><span>Self Rating (1-5)</span></div><div class="notes">Notes / Issues</div></div>
    <div class="grid-row row"><div>Verified recipient ID &amp; relationship</div><div></div><div></div></div>
    <div class="grid-row row"><div>Confirmed correct documents enclosed</div><div></div><div></div></div>
    <div class="grid-row row"><div>Recipient signed the DC logbook</div><div></div><div></div></div>
    <div class="grid-row row"><div>Suggested proofreading before leaving</div><div></div><div></div></div>
  </section>

  <section class="block routing" style="top:305px">
    <div class="bar">
      <span class="icon" style="left:285px;top:-6px">
        <svg width="42" height="40" aria-hidden="true"><ellipse cx="22" cy="18" rx="20" ry="17" fill="#d49a6a"/><path d="M6 28 L2 38 L16 32Z" fill="#d49a6a"/><circle cx="14" cy="18" r="2.5" fill="#fff"/><circle cx="22" cy="18" r="2.5" fill="#fff"/><circle cx="30" cy="18" r="2.5" fill="#fff"/></svg>
      </span>
      <span>6. Routing &amp; Messages</span>
    </div>
    <div class="grid-row head"><div>Task</div><div class="rating"><span>Self Rating (1-5)</span></div><div class="notes">Notes / Issues</div></div>
    <div class="grid-row row"><div>Calls routed appropriately</div><div></div><div></div></div>
    <div class="grid-row row"><div>Messages included all required info</div><div></div><div></div></div>
    <div class="grid-row row"><div>Delivered 95%+ messages in 30 min</div><div></div><div></div></div>
  </section>

  <section class="block status" style="top:535px">
    <div class="bar">
      <span class="icon" style="left:228px;top:-8px" role="img" aria-label="Report sheet icon">
        <svg width="36" height="44"><rect x="2" y="2" width="32" height="40" rx="3" fill="#3a3a3a" transform="rotate(-6 18 22)"/><line x1="9" y1="12" x2="27" y2="11" stroke="#bbb" stroke-width="2"/><line x1="9" y1="19" x2="27" y2="18" stroke="#bbb" stroke-width="2"/><line x1="9" y1="26" x2="27" y2="25" stroke="#bbb" stroke-width="2"/></svg>
      </span>
      <span>Daily Status Summary (Tick One)</span>
    </div>
    <div class="status-row"><span class="tick"></span><span class="level">Excellent</span><span class="desc">All key duties completed, proactive, calm under pressure</span></div>
    <div class="status-row"><span class="tick"></span><span class="level">Satisfactory</span><span class="desc">Most duties completed, minor follow-up needed</span></div>
    <div class="status-row"><span class="tick"></span><span class="level">Needs Support</span><span class="desc">Missed urgent duties, accuracy or stress issues</span></div>
  </section>

  <section class="block reflection" style="top:722px">
    <div class="bar">
      <span class="icon" style="left:322px;top:-10px" role="img" aria-label="Notepad and pen icon">
        <svg width="40" height="46"><rect x="4" y="4" width="30" height="38" rx="3" fill="none" stroke="#3e8e6a" stroke-width="2.5" transform="rotate(-8 19 23)"/><line x1="11" y1="16" x2="26" y2="14" stroke="#3e8e6a" stroke-width="2"/><line x1="11" y1="23" x2="26" y2="21" stroke="#3e8e6a" stroke-width="2"/><line x1="12" y1="30" x2="24" y2="28" stroke="#3e8e6a" stroke-width="2"/></svg>
      </span>
      <span>Daily Reflection</span>
    </div>
    <div class="line-row"><span>What went well today ?</span><span class="fill"></span></div>
    <div class="line-row"><span>Any issues or barriers to note ?</span><span class="fill"></span></div>
    <div class="line-row"><span>Support needed from supervisor ?</span><span class="fill"></span></div>
  </section>

  <section class="block flags" style="top:903px">
    <div class="bar">
      <svg width="22" height="22" aria-hidden="true"><polygon points="11,1 14,8 21,8 15.5,13 17.5,21 11,16.5 4.5,21 6.5,13 1,8 8,8" fill="#fff"/></svg>
      <span>Stars &amp; Flags</span>
      <svg width="30" height="26" aria-hidden="true"><line x1="3" y1="2" x2="6" y2="25" stroke="#fff" stroke-width="2.5"/><path d="M4 3 Q14 -1 18 4 Q22 8 28 3 L29 15 Q22 20 17 15 Q12 11 5 15Z" fill="#fff"/></svg>
      <span>(Supervisor Use Only)</span>
    </div>
    <div class="line-row"><svg width="16" height="16" aria-hidden="true"><polygon points="8,1 10,6 15,6 11,9.5 12.5,15 8,12 3.5,15 5,9.5 1,6 6,6" fill="var(--icon-brown)"/></svg><span>Excellence or above-and-beyond moments</span><span class="fill"></span></div>
    <div class="line-row"><svg width="20" height="20" aria-hidden="true"><line x1="2" y1="2" x2="4" y2="19" stroke="var(--icon-brown)" stroke-width="2"/><path d="M3 3 Q9 0 12 3 Q15 6 19 3 L19 11 Q15 14 12 11 Q8 8 4 11Z" fill="var(--icon-brown)"/></svg><span>Concerns needing follow-up/coaching</span><span class="fill" style="margin-left:14px"></span></div>
  </section>

  <section class="block manager" style="top:1052px">
    <div class="bar">
      <span class="icon" style="left:87px;top:-8px">
        <svg width="40" height="40" aria-hidden="true"><g fill="#5a3a8a"><circle cx="6" cy="8" r="2"/><circle cx="13" cy="4" r="2"/><circle cx="20" cy="2" r="2"/><circle cx="27" cy="4" r="2"/><circle cx="34" cy="8" r="2"/><rect x="6" y="20" width="7" height="16" rx="1"/><path d="M15 20 L21 12 Q24 10 24 15 L23 19 L31 19 Q34 20 33 23 L31 34 Q30 36 27 36 L15 36Z"/></g></svg>
      </span>
      <span>Manager's Overall Rating</span>
    </div>
    <div class="line-row" style="padding-right:20px"><span>Please rate overall performance on a 1-5 scale</span></div>
    <div class="line-row"><span>Manager Overall Rating</span><span class="fill"></span></div>
  </section>

  <section class="sign-box">
    <div class="sign-line"><span class="label">Receptionist Sign.</span><span class="fill"></span></div>
    <div class="sign-line"><span class="label">Supervisor Sign.</span><span class="fill"></span></div>
    <div class="sign-line"><span class="label right">Date</span><span class="fill"></span></div>
  </section>

</main>
</body>
</html>
```